Store Promo Card (already have logo!)

I need a card design (single side) for my online women’s gift shop containing a promotional code to be placed in bags for attendees at an event. I’m flexible on both shape and sizing, but perhaps a 4x6 card.
—It should contain my attached logo, my website (www.corvidtpq.com), and my Instagram handle (@corvidtpq) and promotion language such as “15% off your purchase with code: MIRVOL”.
—I think I would like my logo to be large.
—It should be clean, simple and modern in design and should use the colors from my logo.
—I would like about 3-5 product pictures depending on design.
Target Market(s)
Women ages 30 to 60
Industry/Entity Type
Retail Upscale Gift
Look and feel

```html
<!DOCTYPE html>
<html lang="en">
<head>
<meta charset="utf-8">
<title>Corvid TPQ – Promo Card</title>
<link rel="stylesheet" href="https://fonts.googleapis.com/css2?family=Playfair+Display:wght@800&family=Lato:wght@300;400&family=Allura&display=swap">
<style>
  :root {
    --blush: #e3cfcb;
    --blush-deep: #d9c2bd;
    --ivory: #f8f6f1;
    --charcoal: #606060;
    --ink: #5a5a5a;
    --rule: #9a9a9a;
    --taupe: #b7ad9f;
  }
  * { margin: 0; padding: 0; box-sizing: border-box; }
  html, body { width: 1200px; height: 857px; overflow: hidden; background: var(--ivory); }
  .card {
    position: relative; width: 1200px; height: 857px; overflow: hidden;
    background: var(--ivory); font-family: "Lato", sans-serif; color: var(--ink);
  }
  .blush-field { position: absolute; left: 0; top: 0; width: 682px; height: 857px; background: var(--blush); }
  .v-rule { position: absolute; top: 0; width: 1px; height: 857px; background: var(--rule); }
  .h-rule { position: absolute; left: 811px; width: 350px; height: 1px; background: var(--rule); }

  .brand { position: absolute; left: 82px; top: 78px; width: 468px; text-align: center; color: var(--charcoal); }
  .brand-name { font-family: "Playfair Display", serif; font-weight: 800; font-size: 84px; letter-spacing: 2px; line-height: 1; }
  .brand-tag { display: block; margin-top: 34px; font-family: "Lato", sans-serif; font-weight: 400; font-size: 24px; letter-spacing: 3px; }

  .photo { position: absolute; }
  .photo-fragrance { left: 572px; top: 51px; width: 201px; height: 202px; background: linear-gradient(135deg, #f3eee8 0%, #e9dfd2 55%, #e8b064 100%); }
  .photo-bracelets { left: 572px; top: 275px; width: 201px; height: 199px; background: var(--taupe); }
  .photo-bracelets .inner { position: absolute; left: 24px; top: 24px; right: 24px; bottom: 24px; background: linear-gradient(160deg, #d6b89a, #b88f6c); }
  .photo-cuffs { left: 348px; top: 389px; width: 205px; height: 184px; background: linear-gradient(140deg, #f4f3f1 0%, #e6e4e0 60%, #d9b66f 100%); }
  .photo-candle { left: 348px; top: 595px; width: 205px; height: 205px; background: linear-gradient(180deg, #f4f4f2 0%, #e7e4de 45%, #8a7650 100%); }
  .photo-model { left: 572px; top: 495px; width: 201px; height: 305px; border-bottom-left-radius: 110px; background: linear-gradient(180deg, #8c7462 0%, #c6a38a 30%, #ece5d9 55%, #e3dccf 100%); }

  .arch { position: absolute; left: 82px; top: 440px; width: 244px; height: 363px; background: var(--ivory); border-radius: 122px 122px 0 0; }
  .photo-pouch { left: 82px; top: 660px; width: 244px; height: 143px; background: linear-gradient(180deg, #f8f6f1 0%, #3a3a3a 30%, #141414 100%); }

  .offer-block { position: absolute; left: 853px; top: 0; width: 134px; height: 253px; background: var(--charcoal); }
  .offer-percent { position: absolute; left: 0; width: 134px; top: 168px; text-align: center; color: #fff; font-weight: 300; font-size: 44px; }
  .offer-copy { position: absolute; left: 1013px; top: 115px; font-weight: 400; font-size: 20px; line-height: 29px; color: var(--ink); }

  .products { position: absolute; left: 853px; top: 326px; width: 264px; height: 247px; background: var(--blush-deep); box-shadow: 4px 5px 0 #d6d2cc; overflow: hidden; }
  .products-copy { position: absolute; left: 22px; top: 52px; width: 236px; font-family: "Allura", cursive; font-size: 20px; line-height: 44px; color: #4d4d4d; white-space: nowrap; }
  .leaf-art { position: absolute; left: 980px; top: 318px; width: 140px; height: 78px; background: linear-gradient(110deg, #ffffff 0%, #f1d7d6 50%, #e3b8ba 100%); border-radius: 40px; transform: rotate(-12deg); }

  .contact-title { position: absolute; left: 811px; top: 628px; width: 350px; text-align: center; font-weight: 300; font-size: 52px; letter-spacing: 2px; color: var(--charcoal); line-height: 1; }
  .contact-row { position: absolute; left: 867px; display: flex; align-items: center; gap: 12px; font-size: 21px; color: var(--ink); }
  .contact-row svg { width: 34px; height: 34px; flex: none; }
</style>
</head>
<body>
<div class="card">
  <div class="blush-field"></div>
  <div class="v-rule" style="left:43px"></div>

  <div class="brand">
    <div class="brand-name">CORVID</div>
    <span class="brand-tag">TPQ</span>
  </div>

  <div class="photo photo-fragrance" role="img" aria-label="Fragrance bottle beside an orange on a wooden block"></div>
  <div class="photo photo-bracelets" role="img" aria-label="Stack of gold chain bracelets on a wrist"><div class="inner"></div></div>
  <div class="photo photo-cuffs" role="img" aria-label="Three gold cuff bracelets"></div>
  <div class="photo photo-candle" role="img" aria-label="Scented candle in a glass with black and gold label"></div>
  <div class="photo photo-model" role="img" aria-label="Woman in a cream ribbed tank top wearing a gold necklace"></div>

  <div class="arch"></div>
  <div class="photo photo-pouch" role="img" aria-label="Black canvas zip pouch with white lettering"></div>

  <div class="v-rule" style="left:811px"></div>
  <div class="v-rule" style="left:1161px"></div>

  <div class="offer-block"><div class="offer-percent">15%</div></div>
  <p class="offer-copy">off your<br>purchase<br>with code:<br>MIRVOL</p>

  <div class="h-rule" style="top:287px"></div>

  <div class="products">
    <p class="products-copy">Products<br>Jewelry, Accessories, Apparel,<br>Fragrance, Lingerie,<br>Household products and more.</p>
  </div>
  <div class="leaf-art" role="img" aria-label="Blush pink leaf illustration"></div>

  <div class="h-rule" style="top:610px"></div>
  <h2 class="contact-title">CONTACT</h2>
  <div class="h-rule" style="top:697px"></div>

  <div class="contact-row" style="top:710px">
    <svg viewBox="0 0 34 34" aria-hidden="true"><circle cx="17" cy="17" r="17" fill="#5f5f5f"/><path d="M12 10 L23 17 L18 18.5 L21 24 L19 25 L16 19.5 L12 23 Z" fill="none" stroke="#fff" stroke-width="1.6" stroke-linejoin="round"/></svg>
    <span>www.corvidtpq.com</span>
  </div>

  <div class="h-rule" style="top:757px"></div>

  <div class="contact-row" style="top:770px">
    <svg viewBox="0 0 34 34" aria-hidden="true"><circle cx="17" cy="17" r="17" fill="#5f5f5f"/></svg>
    <span>@corvidtpq</span>
  </div>

  <div class="h-rule" style="top:821px"></div>
</div>
</body>
</html>
```